New Book Cover Design Project

Book Cover with this title and sub title
Where Auntie Found Her Quiet Orchard
The little book to be smart with your money and help the environment.
Walter P. Drune Ph. D.
Edith P. Drune
Picture below would be on the entire front cover. Words somehow incorporated for easy reading.

```html
<!DOCTYPE html>
<html lang="en">
<head>
<meta charset="utf-8">
<title>Where Auntie Found Her Quiet Orchard</title>
<link href="https://fonts.googleapis.com/css2?family=Cinzel:wght@400&display=swap" rel="stylesheet">
<style>
  :root {
    --cover-amber: #e6a20b;
    --ink-white: #ffffff;
    --paper-edge: #fbfaf5;
    --bloom-yellow: #f7d41c;
    --bloom-deep: #eab50d;
    --leaf-shade: #5b5a34;
    --soil-brown: #6b5338;
  }
  html, body {
    margin: 0;
    padding: 0;
    overflow: hidden;
  }
  body {
    width: 840px;
    height: 1200px;
  }
  .cover {
    position: relative;
    width: 840px;
    height: 1200px;
    background: var(--cover-amber);
    overflow: hidden;
    font-family: "Cinzel", "Times New Roman", serif;
    color: var(--ink-white);
  }
  .cover-photo {
    position: absolute;
    left: 118px;
    top: 88px;
    width: 600px;
    height: 586px;
    filter: drop-shadow(2px 3px 4px rgba(90, 55, 0, 0.35));
  }
  .title-block {
    position: absolute;
    left: 0;
    right: 0;
    top: 686px;
    text-align: center;
  }
  .title-small {
    display: block;
    font-size: 32px;
    letter-spacing: 0.5em;
    text-transform: uppercase;
    line-height: 1;
    padding-left: 0.5em;
  }
  .title-large {
    display: block;
    font-size: 76px;
    line-height: 1;
    letter-spacing: 0.01em;
  }
  .title-small.first { margin-bottom: 20px; }
  .title-small.middle { margin: 22px 0 18px; }
  .authors {
    position: absolute;
    left: 0;
    right: 0;
    top: 1090px;
    text-align: center;
    font-size: 29px;
    line-height: 37px;
  }
  .author { display: block; }
</style>
</head>
<body>
  <main class="cover">
    <svg class="cover-photo" viewBox="0 0 600 586" role="img" aria-label="Close-up photograph of a bee on a bright yellow dandelion bloom, with torn paper edges">
      <defs>
        <radialGradient id="bloomGlow" cx="55%" cy="60%" r="70%">
          <stop offset="0%" stop-color="var(--bloom-deep)"/>
          <stop offset="45%" stop-color="var(--bloom-yellow)"/>
          <stop offset="80%" stop-color="#d8b21c"/>
          <stop offset="100%" stop-color="var(--soil-brown)"/>
        </radialGradient>
      </defs>
      <polygon class="torn-edge" fill="var(--paper-edge)"
        points="10,14 60,10 110,16 160,8 210,14 260,10 300,18 350,8 400,14 450,6 500,12 560,4 598,2 594,60 598,120 592,190 597,260 591,330 596,400 590,470 594,530 590,584 540,578 480,582 420,576 360,580 300,574 240,580 180,572 120,578 60,572 30,578 34,520 28,460 34,400 26,340 32,280 24,220 30,160 20,100 26,50" />
      <polygon class="photo-fill" fill="url(#bloomGlow)"
        points="16,20 60,16 110,22 160,14 210,20 260,16 300,24 350,14 400,20 450,12 500,18 560,10 592,8 588,60 592,120 586,190 591,260 585,330 590,400 584,470 588,530 584,578 540,572 480,576 420,570 360,574 300,568 240,574 180,566 120,572 60,566 36,572 40,520 34,460 40,400 32,340 38,280 30,220 36,160 26,100 32,50" />
    </svg>

    <h1 class="title-block">
      <span class="title-small first">Where</span>
      <span class="title-large">Auntie Found</span>
      <span class="title-small middle">Her</span>
      <span class="title-large">Quiet Orchard</span>
    </h1>

    <p class="authors">
      <span class="author">Walter P. Drune Ph. D.</span>
      <span class="author">Edith P. Drune</span>
    </p>
  </main>
</body>
</html>
```